Brochure Cover Design Project

Need a design for our company brochure cover.
We are a mechanical consulting engineering firm ( HVAC, pLUMBING). We have the brochure

Target Market(s)

Architects and Building Owners

Industry/Entity Type

Hvac

```html
<!DOCTYPE html>
<html lang="en">
<head>
<meta charset="utf-8">
<title>Meridian Design Studio – Brochure Cover</title>
<link rel="stylesheet" href="https://fonts.googleapis.com/css2?family=Oswald:wght@500;600;700&family=Source+Sans+3:wght@400;700&display=swap">
<style>
  :root {
    --page-bg: #e9e9e6;
    --green-dark: #2d5a2d;
    --green-mid: #4a8a40;
    --green-light: #b3e28a;
    --green-text: #9ed67a;
    --white: #ffffff;
  }
  * { box-sizing: border-box; margin: 0; padding: 0; }
  html, body {
    width: 1200px; height: 960px; overflow: hidden;
    background: var(--page-bg);
  }
  .brochure {
    position: absolute; left: 5px; top: 95px;
    width: 1190px; height: 770px;
    background: var(--white);
    box-shadow: 0 4px 16px rgba(0,0,0,.18);
    font-family: "Oswald", sans-serif;
  }
  .block { position: absolute; }

  .services-band {
    left: 0; top: 0; width: 595px; height: 180px;
    background: var(--green-dark);
  }
  .services-title {
    position: absolute; left: 0; right: 0; top: 118px;
    text-align: center; color: var(--green-text);
    font-size: 36px; font-weight: 700; letter-spacing: .5px; line-height: 1.2;
  }

  .tile {
    display: flex; align-items: center; justify-content: center;
    text-align: center; font-size: 27px; font-weight: 700; line-height: 1.3;
  }
  .tile--light { background: var(--green-light); color: var(--green-dark); }
  .tile--mid { background: var(--green-mid); color: var(--green-light); }

  .front-brand {
    left: 595px; top: 0; width: 595px; height: 191px;
    display: flex; align-items: center; justify-content: center; gap: 14px;
  }
  .brand-mark { flex: none; width: 32px; height: 32px; background: var(--green-mid); }
  .brand-name {
    font-size: 40px; font-weight: 700; color: var(--green-dark);
    letter-spacing: 1px; text-transform: uppercase; white-space: nowrap; line-height: 1.2;
  }

  .contact-band {
    left: 0; top: 532px; width: 1190px; height: 238px;
    background: var(--green-dark);
  }
  .back-brand {
    position: absolute; left: 108px; top: 44px; width: 400px; height: 78px;
    display: flex; align-items: center; justify-content: center; gap: 10px;
  }
  .back-brand .brand-mark { width: 18px; height: 18px; background: var(--green-light); }
  .back-brand .brand-name { font-size: 24px; color: var(--green-light); }

  .contact {
    position: absolute; top: 150px;
    font-family: "Source Sans 3", sans-serif; font-size: 17px; line-height: 22px;
    color: var(--green-light); white-space: nowrap;
  }
  .contact--address { right: 900px; text-align: right; }
  .contact--phone { left: 342px; }
  .contact-divider {
    position: absolute; left: 314px; top: 150px; width: 1px; height: 54px;
    background: var(--green-mid);
  }
  .tagline {
    position: absolute; left: 595px; width: 595px; top: 48px;
    text-align: center; color: var(--white);
    font-size: 28px; font-weight: 600; letter-spacing: .3px; line-height: 1.2; white-space: nowrap;
  }
  .website {
    position: absolute; left: 595px; width: 595px; top: 118px;
    text-align: center; color: var(--green-text);
    font-family: "Source Sans 3", sans-serif; font-size: 25px; font-weight: 700; line-height: 1.2;
  }
</style>
</head>
<body>
  <main class="brochure">
    <section class="block services-band">
      <h2 class="services-title">SERVICES</h2>
    </section>

    <div class="block tile tile--light" style="left:0;top:191px;width:298px;height:160px;">Mechanical<br>HVAC</div>
    <div class="block tile tile--mid" style="left:312px;top:191px;width:283px;height:160px;">Fire Protection</div>
    <div class="block tile tile--mid" style="left:0;top:362px;width:298px;height:160px;">Mechanical<br>Plumbing</div>
    <div class="block tile tile--light" style="left:312px;top:362px;width:283px;height:160px;">Electrical</div>

    <div class="block front-brand">
      <span class="brand-mark"></span>
      <span class="brand-name">Meridian Design Studio</span>
    </div>

    <div class="block photo" role="img" aria-label="Photo of a theatre auditorium interior with rows of seats"
         style="left:595px;top:191px;width:298px;height:160px;background:linear-gradient(160deg,#3b5a8a 0%,#7a3a2a 45%,#2a2a30 100%);"></div>
    <div class="block photo" role="img" aria-label="Photo of a modern glass building lit at dusk"
         style="left:905px;top:191px;width:285px;height:160px;background:linear-gradient(180deg,#2d4f8a 0%,#5a6e8e 55%,#3a3a3a 100%);"></div>
    <div class="block photo" role="img" aria-label="Photo of a white glass conservatory with domes"
         style="left:595px;top:362px;width:298px;height:160px;background:linear-gradient(180deg,#b9cbe0 0%,#e4e8ea 50%,#7b8a6a 100%);"></div>
    <div class="block photo" role="img" aria-label="Photo of a modern stone and glass school building"
         style="left:905px;top:362px;width:285px;height:160px;background:linear-gradient(180deg,#d8e0e6 0%,#c4b596 55%,#8a8060 100%);"></div>

    <footer class="block contact-band">
      <div class="back-brand">
        <span class="brand-mark"></span>
        <span class="brand-name">Meridian Design Studio</span>
      </div>
      <p class="contact contact--address">2240 Harbor View Rd. Ste. 210<br>Lakemont, CA 94820</p>
      <span class="contact-divider"></span>
      <p class="contact contact--phone">P:&nbsp; 555-482-7300 x 214<br>F:&nbsp; 555-482-7391</p>
      <p class="tagline">BUILDING SYSTEMS THAT QUIETLY PERFORM</p>
      <p class="website">www.meridian-ds.com</p>
    </footer>
  </main>
</body>
</html>
```